Business Card Design

We require a business card design for a law firm, our signature colours are maroon and cream. Our slogan is "From our family to yours", we would like the cards to be professional however feminine at the same time.

Industry/Entity Type

Business

Contact Information for Business Card

Helena Brockett & Associates Lawyers & Conveyancers, Helena Brockett LL.B. Principal Solicitor, 17 Thornbury Street, Kelvale NSW 2239

Logo styles of interest
Emblem Logo
Abstract Logo
Wordmark Logo

```html
<!DOCTYPE html>
<html lang="en">
<head>
<meta charset="utf-8">
<title>Helena Brockett &amp; Associates — Business Card</title>
<link rel="stylesheet" href="https://fonts.googleapis.com/css2?family=Encode+Sans+Semi+Condensed:wght@500&family=Roboto+Slab:wght@300;700&display=swap">
<style>
  :root {
    --cream: #f7de95;
    --maroon: #8c1b20;
    --page: #ffffff;
  }
  html, body {
    margin: 0;
    padding: 0;
    width: 1200px;
    height: 708px;
    overflow: hidden;
    background: var(--page);
  }
  .card {
    position: absolute;
    left: 52px;
    top: 44px;
    width: 1080px;
    height: 616px;
    background: var(--cream);
    border-radius: 32px;
    overflow: hidden;
  }
  .brand-band {
    position: absolute;
    left: 0;
    top: 172px;
    width: 448px;
    height: 260px;
    background: var(--maroon);
  }
  .brand-mark {
    position: absolute;
    left: 50px;
    top: 52px;
  }
  .slogan {
    position: absolute;
    left: 232px;
    top: 60px;
    margin: 0;
    font-family: "Encode Sans Semi Condensed", "Roboto Condensed", sans-serif;
    font-weight: 500;
    font-size: 40px;
    line-height: 45px;
    color: var(--cream);
  }
  .edge-bar {
    position: absolute;
    right: 0;
    top: 172px;
    width: 30px;
    height: 260px;
    background: var(--maroon);
  }
  .contact {
    position: absolute;
    right: 74px;
    top: 160px;
    text-align: right;
    font-family: "Roboto Slab", serif;
    color: var(--maroon);
  }
  .firm-name {
    margin: 0;
    font-weight: 300;
    font-size: 34px;
    line-height: 37px;
  }
  .person-name {
    margin: 28px 0 0;
    font-weight: 700;
    font-size: 29px;
    line-height: 34px;
  }
  .details {
    margin: 20px 0 0;
    font-weight: 300;
    font-size: 33px;
    line-height: 42px;
  }
</style>
</head>
<body>
  <div class="card">
    <div class="brand-band">
      <svg class="brand-mark" width="156" height="156" viewBox="0 0 156 156" aria-hidden="true">
        <circle cx="78" cy="78" r="76" fill="none" stroke="var(--cream)" stroke-width="3"/>
      </svg>
      <p class="slogan">From Our<br>Family<br>To Yours</p>
    </div>
    <div class="edge-bar"></div>
    <div class="contact">
      <p class="firm-name">Helena Brockett &amp; Associates<br>Lawyers &amp; Conveyancers</p>
      <p class="person-name">Helena Brockett</p>
      <p class="details">LL.B. Principal Solicitor,<br>17 Thornbury Street,<br>Kelvale NSW 2239</p>
    </div>
  </div>
</body>
</html>
```